Modern Website Design for an Online Travel Agency.. Design Only!!

Hi there!

We are building an website for our travel agency that caters to tourists traveling to the Cayman Islands. We provide travel information and take bookings for various tours available here.

We need designs for 8 different web page layouts. You can see the layout specifications in two attached documents. We do not have a need for the coding to be done. This will simply act as a blueprint for our developer to build from.

The important pages are the 'Home Page' 'checkout page' and the ‘Checkout Page’ (Page 1 & 10 in the PDF ‘Website Layout’)

The MOST important page is ‘Tour Search Page’ (page 6)

If you intend on only submitting one page design, please submit a design for page 6. Be aware though, the more of these 3 page designs you submit, the more likely we are to move forward with you!

At this stage, we are simply looking to develop the most aesthetic website design layout possible.

- The website should be colour coordinated with the logo. You can most certainly use other colours if you feel they complement the overall design of the website well.

- Everything must be laid out in an EXTREMELY simple & ‘easy to navigate’ way. The key is simplicity & Functionality. There is no need for messy or elaborate graphics.

- The website MUST have a VERY clean and modern appearance.

- We want the main background to be white, but you can use light grey in places to compliment or add dimension if you feel necessary.

- We will appreciate a good use of shadows and especially a good use of icons. (You can see examples of icons we have already designed, we are definitely open to new icon design concepts too)

- We will reward imagination and original thinking! Essentially we want a website with a creative touch and unique design elements, whilst maintaining that clean and simple layout.

- Most importantly!! - Paying attention to the small details will be highly rewarded (A well balanced and seamless use of fonts, colours, dimensions, shadowing, positioning, etc)

If you have any questions, please don’t hesitate to ask.

We’re excited to see your design submissions!

Thank you!!

You can find all the support documents and content at: https://www.filevorra.net/sh/9qm2rtwplexan7c/QQBmTtZnPdLsWEGxvvaJpLmRw?dl=0

Target Market(s)

Tourists

Industry/Entity Type

Travel

Number of Pages Required

5+ page

Font styles to use
Sans Serif

Colors

Designer to choose colors to be used in the design.

Requirements
Must have
• Must be very clean and modern.
• Must be simple and bold
• Must be color coordinated in a way that makes sense
• White background
Nice to have
• Good use of shadows and Icons
Should not have
• Over use of messy graphics
• And design layout which is not right angled (using anything but vertical or horizontal for the edges in the design)

```html
<!DOCTYPE html>
<html lang="en">
<head>
<meta charset="utf-8">
<title>IsleRoute – Let's Book Your Trip</title>
<link href="https://fonts.googleapis.com/css2?family=Lato:wght@300;400;700&display=swap" rel="stylesheet">
<style>
:root{
  --blue:#0a6fd8;
  --blue-deep:#0b5fb8;
  --green:#8cc63f;
  --green-dark:#7cb82f;
  --ink:#1f1f1f;
  --muted:#555;
  --line:#ececec;
  --grey-bg:#f6f6f6;
  --footer:#17161c;
  --white:#fff;
}
*{box-sizing:border-box;margin:0;padding:0}
html,body{width:1200px;height:2756px;overflow:hidden;background:var(--white)}
body{font-family:'Lato',sans-serif;color:var(--ink);position:relative}
a{color:inherit;text-decoration:none}

.topbar{height:61px;display:flex;align-items:center;padding:0 172px;justify-content:space-between}
.brand{display:flex;align-items:center;gap:8px;font-size:24px;font-weight:700;color:var(--blue)}
.brand-mark{width:30px;height:30px;background:var(--green);border-radius:4px}
.topbar-right{display:flex;align-items:center;gap:12px;font-size:12px}
.social-dot{width:11px;height:11px;border-radius:50%;background:var(--blue)}
.currency{margin:0 22px 0 20px}
.btn-login{background:var(--green);color:#fff;width:79px;height:29px;display:flex;align-items:center;justify-content:center;font-size:12px}

.hero{position:relative;height:515px;background:linear-gradient(180deg,#0c4f8a 0%,#1b72a8 30%,#2a8fa0 45%,#1ca5a0 62%,#179b96 100%)}
.hero-photo{position:absolute;inset:0;background:linear-gradient(180deg,rgba(10,60,110,.35),rgba(0,0,0,0) 40%,rgba(20,160,150,.2))}
.mainnav{position:relative;height:49px;display:flex;align-items:center;padding:0 172px;border-bottom:1px solid rgba(255,255,255,.25);color:#fff;font-size:12px}
.mainnav a{margin-right:26px}
.nav-dest{margin-left:auto;display:flex;align-items:center;gap:8px}
.hero-title{position:absolute;top:207px;left:0;width:100%;text-align:center;color:#fff;font-size:38px;font-weight:700;line-height:46px;z-index:1}
.search{position:absolute;top:274px;left:207px;width:786px;height:39px;background:#fff;display:flex;font-size:11px;color:#222;z-index:1}
.search-field{display:flex;align-items:center;gap:12px;padding-left:16px;border-right:1px solid #ddd;margin:6px 0}
.search-btn{margin-left:auto;width:160px;background:var(--green);color:#fff;font-size:14px;display:flex;align-items:center;justify-content:center;border:0;font-family:inherit}
.hero-caption{position:absolute;top:334px;left:0;width:100%;text-align:center;color:#fff;font-size:13px;z-index:1}

.welcome{height:266px;background:var(--blue);color:#fff;text-align:center;padding-top:48px}
.welcome h2{font-size:24px;font-weight:400}
.welcome p{width:780px;margin:22px auto 0;font-size:13px;line-height:24px;font-weight:300}
.btn-green{display:inline-block;background:var(--green);color:#fff;font-size:12px;height:33px;line-height:33px}
.welcome .btn-green{margin-top:24px;width:110px}

.section-title{text-align:center;font-size:24px;font-weight:400}
.steps{padding-top:40px}
.step-grid{display:grid;grid-template-columns:417px 418px;gap:37px 21px;margin:57px 0 0 172px}
.step-card{position:relative;height:228px;border:1px solid var(--line);box-shadow:0 2px 6px rgba(0,0,0,.04);padding:50px 0 0 19px}
.step-tag{position:absolute;top:-16px;left:29px;width:93px;height:32px;background:var(--blue);color:#fff;font-size:18px;display:flex;align-items:center;justify-content:center}
.step-card h3{font-size:18px;font-weight:400;color:var(--blue);line-height:23px;width:160px;position:relative;z-index:1}
.step-card p{font-size:9.5px;line-height:16.5px;color:var(--muted);width:200px;margin-top:14px;position:relative;z-index:1}
.step-actions{position:absolute;left:19px;top:172px;display:flex;gap:8px}
.btn-sm{height:22px;line-height:22px;padding:0 9px;font-size:8px;color:#fff}
.btn-sm.green{background:var(--green-dark)}
.btn-sm.blue{background:var(--blue)}
.step-art{position:absolute;right:12px;top:38px;width:126px;height:140px;border-radius:50%;background:radial-gradient(circle,#e6f3fb 0%,#f4faf0 60%,#fff 100%)}

.destinations{padding-top:113px}
.dest-grid{display:flex;gap:22px;margin:27px 0 0 172px}
.dest-card{position:relative;width:271px;height:358px;display:flex;flex-direction:column;justify-content:flex-end;align-items:center;padding-bottom:30px;color:#fff}
.dest-card h4{font-size:18px;font-weight:400}
.dest-card span{font-size:11px;margin-top:3px}
.dest-a{background:linear-gradient(180deg,#cfe2f2 0%,#2c73a8 35%,#1a4f86 70%,#0b1c3a 100%)}
.dest-b{background:linear-gradient(180deg,#c9d8e2 0%,#2e7a3f 25%,#3fc7c2 45%,#21a49b 75%,#0f4d57 100%)}
.dest-c{background:linear-gradient(180deg,#6f9fd3 0%,#1d5fa8 35%,#1b4e7a 60%,#0a1d33 100%)}

.todo{margin-top:45px;height:356px;background:var(--grey-bg);padding-top:46px;position:relative}
.todo-grid{display:flex;gap:22px;margin:32px 0 0 172px}
.todo-card{width:271px;height:207px}
.todo-a{background:linear-gradient(180deg,#8fb9e8 0%,#d9e8f6 45%,#2f8fc8 75%,#1b6fa8 100%)}
.todo-b{background:linear-gradient(180deg,#2d6fb8 0%,#c7d9ec 40%,#5d93c3 70%,#2c6396 100%)}
.todo-c{background:linear-gradient(180deg,#2aa2c6 0%,#1b86b3 50%,#6b4a2a 85%,#3a3a3a 100%)}
.todo-next{position:absolute;left:1056px;top:225px}

.footer{position:absolute;top:2378px;left:0;width:1200px;height:378px;background:var(--footer);color:#fff;font-size:12px}
.footer-cols{position:absolute;top:78px;left:171px;display:flex}
.footer-col h5{font-size:14px;font-weight:700;margin-bottom:22px}
.footer-col li{list-style:none;margin-bottom:9px}
.col-contact{width:222px}.col-links{width:217px}.col-dest{width:219px}
.contact-label{text-decoration:underline;margin-bottom:4px}
.contact-value{margin-bottom:22px}
.follow{display:flex;gap:8px;margin-top:-2px}
.follow span{width:30px;height:30px;border-radius:50%;background:#fff}
.copyright{position:absolute;bottom:20px;width:100%;text-align:center}
</style>
</head>
<body>

<header class="topbar">
  <a class="brand" href="#"><span class="brand-mark"></span>IsleRoute</a>
  <div class="topbar-right">
    <span class="social-dot"></span><span class="social-dot"></span><span class="social-dot"></span><span class="social-dot"></span>
    <span class="currency">$USD</span>
    <a class="btn-login" href="#">Log In</a>
  </div>
</header>

<section class="hero">
  <div class="hero-photo" role="img" aria-label="Tropical beach with palm trees and turquoise sea"></div>
  <nav class="mainnav">
    <a href="#">Discover Cayman</a><a href="#">Thing to Do</a><a href="#">My Trip Planner</a><a href="#">Map</a><a href="#">Contact Us</a>
    <span class="nav-dest">
      <svg width="13" height="13" viewBox="0 0 14 14" fill="none" stroke="#fff"><circle cx="7" cy="7" r="6"/><path d="M1 7h12M7 1c3 3 3 9 0 12M7 1c-3 3-3 9 0 12"/></svg>
      Dstination
      <svg width="8" height="5" viewBox="0 0 8 5"><path d="M0 0h8L4 5z" fill="#fff"/></svg>
    </span>
  </nav>
  <h1 class="hero-title">Let's Book Your Trip</h1>
  <form class="search">
    <div class="search-field" style="width:172px">
      <svg width="10" height="14" viewBox="0 0 10 14"><path d="M5 0a5 5 0 015 5c0 4-5 9-5 9S0 9 0 5a5 5 0 015-5z" fill="#bbb"/></svg>Location</div>
    <div class="search-field" style="width:255px">
      <svg width="12" height="13" viewBox="0 0 12 13"><circle cx="6" cy="3.5" r="3.5" fill="#bbb"/><path d="M0 13a6 5 0 0112 0z" fill="#bbb"/></svg>0 - Adult<span style="margin-left:48px">0 - Child</span></div>
    <div class="search-field" style="border:0">
      <svg width="14" height="11" viewBox="0 0 14 11"><rect y="4" width="14" height="5" fill="#bbb"/><rect x="1" y="1" width="12" height="3" fill="#ccc"/></svg>Bed</div>
    <button class="search-btn" type="button">Search</button>
  </form>
  <p class="hero-caption">Aenean sollicitudin, lorem quis bibendum auctor, nisi elit consequat ipsum, nec sagittis sem nibh id elit.</p>
</section>

<section class="welcome">
  <h2>Welcome to IsleRoute</h2>
  <p>Duis sed odio sit amet nibh vulputate cursus a sit amet mauris. Morbi accumsan ipsum velit. Nam nec tellus a odio tincidunt auctor a ornare odio. Sed non&nbsp; mauris vitae erat consequat auctor eu in elit. Class aptent taciti sociosqu ad litora torquent per conubia nostra, per inceptos himenaeos. Mauris in erat justo. Nullam ac urna eu felis dapibus condimentum sit amet a augue.</p>
  <a class="btn-green" href="#">Read More</a>
</section>

<section class="steps">
  <h2 class="section-title">Follow The Easy 4 Step &amp; Relax</h2>
  <div class="step-grid">
    <article class="step-card"><span class="step-tag">Step 1</span>
      <div class="step-art" role="img" aria-label="Illustration of a traveller browsing activities on a laptop"></div>
      <h3>Choose Your Favorite Activities</h3>
      <p style="width:200px">Discover everything you need to know about travel &amp; safety in the Cayman Islands and browse every fun activity available here</p>
      <div class="step-actions"><a class="btn-sm green" href="#">Learn About Cayman</a><a class="btn-sm blue" href="#">Find Things To Go</a></div>
    </article>
    <article class="step-card"><span class="step-tag">Step 2</span>
      <div class="step-art" role="img" aria-label="Illustration of a traveller planning a trip on a large screen"></div>
      <h3>Use Our Online Travel PLanner</h3>
      <p style="width:248px">Organize your favorite activities on our user-friendly trip planner to effortlessly design your perfect vacation. Use our planner to easily budget your entire trip</p>
      <div class="step-actions"><a class="btn-sm green" href="#">Learn About Cayman</a><a class="btn-sm blue" href="#">Find Things To Go</a></div>
    </article>
    <article class="step-card"><span class="step-tag">Step 3</span>
      <div class="step-art" role="img" aria-label="Illustration of travellers handing over bookings"></div>
      <h3>We Make&nbsp; All The Arrangement</h3>
      <p style="width:240px">Keep the fun of planning and we'll deal with the hard work and handle all your booking arrangements. Best of all, our services are 100% FREE</p>
      <div class="step-actions"><a class="btn-sm green" href="#">Learn About Cayman</a><a class="btn-sm blue" href="#">Find Things To Go</a></div>
    </article>
    <article class="step-card"><span class="step-tag">Step 4</span>
      <div class="step-art" role="img" aria-label="Illustration of people relaxing on a beach"></div>
      <h3>Relax &amp; Enjoy Your Vacation</h3>
      <p style="width:232px">Consider us your guardian angels during your stay! We continue to offer support throughout your trip, so you can truly enjoy your vacation, stress free!</p>
      <div class="step-actions"><a class="btn-sm green" href="#">Learn About Cayman</a><a class="btn-sm blue" href="#">Find Things To Go</a></div>
    </article>
  </div>
</section>

<section class="destinations">
  <h2 class="section-title">Popular Destination</h2>
  <div class="dest-grid">
    <a class="dest-card dest-a" href="#" role="img" aria-label="Aerial view of Grand Cayman"><h4>Grand Cayman</h4><span>89 Activities</span></a>
    <a class="dest-card dest-b" href="#" role="img" aria-label="Kayakers in turquoise water off Little Cayman"><h4>Little Cayman</h4><span>6 Activities</span></a>
    <a class="dest-card dest-c" href="#" role="img" aria-label="Aerial view of Cayman Brac coastline"><h4>Cayman Brac</h4><span>9 Activities</span></a>
  </div>
</section>

<section class="todo">
  <h2 class="section-title">Things To Do</h2>
  <div class="todo-grid">
    <div class="todo-card todo-a" role="img" aria-label="Boy jumping into the sea"></div>
    <div class="todo-card todo-b" role="img" aria-label="Group of friends jumping on the beach"></div>
    <div class="todo-card todo-c" role="img" aria-label="Snorkellers over a coral reef"></div>
  </div>
  <svg class="todo-next" width="22" height="14" viewBox="0 0 22 14" fill="none" stroke="#222" stroke-width="1.5"><path d="M0 7h20M14 1l6 6-6 6"/></svg>
</section>

<footer class="footer">
  <div class="footer-cols">
    <div class="footer-col col-contact"><h5>Contact</h5>
      <p class="contact-label">Call:</p><p class="contact-value">+0100 555 0199</p>
      <p class="contact-label">Mail:</p><p class="contact-value">hello@isleroute-mail.net</p></div>
    <div class="footer-col col-links"><h5>Quick Links</h5>
      <ul><li>Discover Cayman</li><li>Thing to Do</li><li>My Trip Planner</li><li>Map</li></ul></div>
    <div class="footer-col col-dest"><h5>Destination</h5>
      <ul><li>Grand Cayman</li><li>Little Cayman</li><li>Cayman Barc</li></ul></div>
    <div class="footer-col"><h5>Follow Us On</h5>
      <div class="follow"><span></span><span></span><span></span><span></span></div></div>
  </div>
  <p class="copyright">© Copyrights 2019 IsleRoute. All Rights Reserved</p>
</footer>

</body>
</html>
```